Electronics Recycling and IT Asset Disposition Flyer and Brochure Design

We need a 2 side A5 Flyer and 4 side A4 folder( brochure) for our electronics waste recycling and IT asset management and disposition business.
Our business provides free electronics waste recycling for companies, schools, learning institutions,councils, IT companies and government sectors. Many people are ignorant of responsible recycling of electronics which could harm our health if not treated properly.
The list of other services attached in the pdf.
We provide an end to end and tailored solution for our customers from collection, logistics, data sanitisation, remarketing and recycling.

The Flyer should create awareness of responsible electronics recycling and drive the audience to contact us or go to our website to learn more about the company and services.A brief list of services should also be included in the flyer.The goal is to get the audience to contact us to enquire more about our services.

The Brochure should include all the above plus provide more details about the company, processes, services,contact details (fb, linkedin,Twitter). The goal is to convert the audience to customers for recycling and provide other services as added services.

The final design for both flyer and brochure should communicate responsible recycling of electronic scrap and tailored solution for every organisation.

The company website is www.kelvora-scrap.com.au based in Australia. We serve clients nationwide.

Target Market(s)

IT companies, Corporate, schools and learning institutions, government sector

Industry/Entity Type

Recycling

Contact Information for Business Card

Name: Darren Okefield
email: darren@kelvora-scrap.com.au
website: www.kelvora-scrap.com.au
mobile: +614 173 60294
Phone: 1300 46 2587

Font styles to use
Serif

Requirements
Must have
• I would like the designs to have more images and icons
Nice to have
Should not have
• none

```html
<!DOCTYPE html>
<html lang="en">
<head>
<meta charset="utf-8">
<title>Kelvora Scrap – Brochure Spread</title>
<link rel="stylesheet" href="https://fonts.googleapis.com/css2?family=Didact+Gothic&family=Mulish:wght@600;700;800&family=PT+Sans+Narrow:wght@700&display=swap">
<style>
:root{
  --green:#5cb23a;
  --green-dark:#3f8f2a;
  --teal:#178a4a;
  --forest:#1f4a22;
  --slate:#6e6e6e;
  --ink:#2b2b2b;
  --grey-band:#ececec;
  --grey-panel:#f1f1f1;
  --white:#ffffff;
}
*{margin:0;padding:0;box-sizing:border-box}
html,body{width:1200px;height:767px;overflow:hidden;background:var(--white)}
body{position:relative;font-family:"Didact Gothic",sans-serif;color:var(--ink)}
.page{position:absolute;top:0;height:767px;width:515px;background:var(--white);overflow:hidden}
.page--left{left:0}
.page--right{left:685px}
.top-tab{position:absolute;top:40px;height:6px;width:142px;background:var(--green)}
.page--left .top-tab{left:188px}
.page--right .top-tab{left:185px}

.hero-photo{position:absolute;left:0;top:80px;width:515px;height:205px;
  background:radial-gradient(circle at 60% 55%,#4a8a3a 0%,#1f4a22 45%,#0e2414 100%)}
.brand-badge{position:absolute;left:205px;top:62px;width:92px;height:92px;border-radius:50%;
  background:var(--white);border:2px solid var(--green);display:flex;align-items:center;justify-content:center;text-align:center}
.brand-name{font-family:"Mulish",sans-serif;font-weight:800;font-size:14px;line-height:1.1;color:var(--green)}

.section-band{position:absolute;left:0;top:285px;width:515px;height:28px;background:var(--green);
  color:var(--white);font-family:"Mulish",sans-serif;font-weight:800;font-size:20px;text-align:center;line-height:28px}
.about{position:absolute;left:0;top:313px;width:515px;height:190px;background:var(--grey-panel);padding:9px 62px 0 62px;font-size:8.4px;line-height:1.22;color:#333;text-align:justify}
.about p{margin-bottom:8px}
.about .intro{text-align:center}
.about u{text-decoration:underline}

.quote{position:absolute;left:62px;top:578px;font-family:"PT Sans Narrow",sans-serif;font-weight:700;font-size:21px;line-height:1.25;color:var(--green)}
.quote span{display:block;padding-left:4px}
.cycle{position:absolute;left:0;top:500px}

.footer-bars{position:absolute;left:0;bottom:0;width:515px;height:12px;display:flex}
.footer-bars i{display:block;height:100%}

.title{position:absolute;left:0;width:515px;top:66px;text-align:center;font-family:"Mulish",sans-serif;font-weight:700;font-size:22px;color:var(--green)}
.icon-rail{position:absolute;left:0;top:90px}
.services{position:absolute;left:0;top:143px;width:515px}
.service{position:relative;padding:6px 20px 0 127px;font-size:8px;line-height:1.22;color:#333}
.service:nth-child(odd){background:var(--grey-band)}
.service:nth-child(1){height:73px}
.service:nth-child(2){height:71px}
.service:nth-child(3){height:66px}
.service:nth-child(4){height:65px}
.service:nth-child(5){height:69px}
.service:nth-child(6){height:61px}
.service h3{font-family:"Mulish",sans-serif;font-weight:700;font-size:13px;color:var(--green);margin-bottom:3px}
.service ul{list-style:none}
.service li{padding-left:8px;text-indent:-8px}
.service li::before{content:"•";margin-right:5px}
.service .s-icon{position:absolute;left:66px;top:50%;transform:translateY(-50%)}
.industries{position:absolute;left:0;top:565px;width:515px;height:175px;background:var(--grey-band);text-align:center;padding:16px 20px 0}
.industries h3{font-family:"Mulish",sans-serif;font-weight:700;font-size:14px;color:var(--green);margin-bottom:2px}
.industries p{font-size:8.2px;line-height:1.25;text-align:justify}
.industries .lead{text-align:left;margin:6px 0 8px 38px}
.industries ul{list-style:none;text-align:left;margin-left:70px;font-size:8.2px;line-height:1.2}
.industries li::before{content:"";display:inline-block;width:5px;height:5px;background:var(--green);margin-right:10px}
.factory{position:absolute;left:257px;top:548px;transform:translateX(-50%)}
.contact-row{position:absolute;left:0;top:738px;width:515px;display:flex;justify-content:space-between;padding:0 18px 0 45px;font-size:8.4px;color:var(--green-dark)}
.contact-row span{display:flex;align-items:center;gap:6px}
</style>
</head>
<body>

<section class="page page--left">
  <div class="top-tab"></div>
  <div class="hero-photo" role="img" aria-label="Close-up photograph of a green circuit board with chips and components"></div>
  <div class="brand-badge"><span class="brand-name">Kelvora<br>Scrap</span></div>
  <h2 class="section-band">Who We Are</h2>
  <div class="about">
    <p class="intro">Kelvora Scrap is a full service IT asset disposition, electronics waste recycling and electronics scrap purchasing company in Australia.</p>
    <p><u>Our vision</u> is to become an industry leader by building genuine relationships with clients based on integrity, service quality and consistency, as well as maximizing value recovery.</p>
    <p><u>Our focus</u> is to reduce electronic waste generation through creating awareness in organisations and community about the importance of responsible recycling of electronics waste. Our goal is to provide end-to-end solution in e-waste management through established processes and technological innovations, drive higher returns for our customers and enhance conservation of raw metals within our ecosystem.</p>
    <p><u>Our team</u> of dedicated engineers and professionals work with companies, government offices, institutions and SMEs across Australia to provide personalised IT asset disposal and e-waste management solutions to suit their needs. Our experince and knowledge in this industry will help us to understand and provide innovative solutions to manage your end of life IT assets. We aim at maximising returns and providing cost effective ways to ensure a positive impact on your bottom-line.</p>
  </div>

  <div class="quote">“BE RESPONSIBLE<span>TODAY FOR A BETTER</span><span>FUTURE TOMORROW”</span></div>

  <svg class="cycle" width="515" height="255" viewBox="0 500 515 255" aria-label="E-waste recycling cycle: reuse, recover, recycle">
    <path d="M254.8,659 A112,112 0 0 1 448.8,558 L399.8,599.1 A48,48 0 0 0 316.6,642.4 Z" fill="#5cb23a"/>
    <path d="M448.8,558 A112,112 0 0 1 454.7,694.2 L402.3,657.5 A48,48 0 0 0 399.8,599.1 Z" fill="#fff" stroke="#d4d4d4" stroke-width="1.5"/>
    <path d="M454.7,694.2 A112,112 0 0 1 254.8,659 L316.6,642.4 A48,48 0 0 0 402.3,657.5 Z" fill="#6e6e6e"/>
    <circle cx="363" cy="630" r="44" fill="#fff" stroke="#d6d6d6" stroke-width="3"/>
    <text x="363" y="626" text-anchor="middle" font-family="Didact Gothic, sans-serif" font-size="12" fill="#222">E-waste</text>
    <text x="363" y="641" text-anchor="middle" font-family="Didact Gothic, sans-serif" font-size="12" fill="#222">Recycling</text>

    <circle cx="318" cy="544" r="6" fill="none" stroke="#fff" stroke-width="2"/>
    <text x="330" y="556" font-family="Mulish, sans-serif" font-weight="800" font-size="30" fill="#fff">01</text>
    <text x="280" y="574" font-family="Mulish, sans-serif" font-weight="700" font-size="9" fill="#fff">REUSE</text>
    <text font-family="Didact Gothic, sans-serif" font-size="4.6" fill="#fff">
      <tspan x="272" y="584">Reuse: the first step is</tspan>
      <tspan x="272" y="590">to inspect each device,</tspan>
      <tspan x="272" y="596">check that it works and</tspan>
      <tspan x="272" y="602">decide its value for</tspan>
      <tspan x="272" y="608">resale or further use.</tspan>
    </text>

    <g stroke="#333" stroke-width="2.2" stroke-linecap="round"><line x1="432" y1="570" x2="444" y2="582"/><line x1="444" y1="570" x2="432" y2="582"/></g>
    <text x="411" y="598" font-family="Mulish, sans-serif" font-weight="700" font-size="8.5" fill="#444">RECOVER</text>
    <text font-family="Didact Gothic, sans-serif" font-size="4.6" fill="#666">
      <tspan x="418" y="608">Recover: items that fail</tspan>
      <tspan x="418" y="614">first checks are sorted</tspan>
      <tspan x="418" y="620">for careful dismantling.</tspan>
    </text>
    <text x="423" y="667" font-family="Mulish, sans-serif" font-weight="800" font-size="28" fill="#555">02</text>

    <text x="290" y="700" font-family="Mulish, sans-serif" font-weight="800" font-size="28" fill="#fff">03</text>
    <text x="332" y="698" font-family="Mulish, sans-serif" font-weight="700" font-size="8.5" fill="#fff">RECYCLE</text>
    <circle cx="412" cy="700" r="8" fill="none" stroke="#fff" stroke-width="2" stroke-dasharray="10 3"/>
    <text font-family="Didact Gothic, sans-serif" font-size="4.6" fill="#fff">
      <tspan x="320" y="713">Recycle: parts go to approved</tspan>
      <tspan x="320" y="719">refiners to be made into</tspan>
      <tspan x="320" y="725">new products.</tspan>
    </text>
  </svg>

  <div class="footer-bars">
    <i style="width:26%;background:var(--green)"></i><i style="width:18%;background:var(--teal)"></i><i style="width:12%;background:var(--forest)"></i><i style="width:44%;background:var(--slate)"></i>
  </div>
</section>

<section class="page page--right">
  <div class="top-tab"></div>
  <h1 class="title">Service Offering</h1>
  <svg class="icon-rail" width="515" height="45" viewBox="0 0 515 45" aria-hidden="true">
    <line x1="0" y1="16" x2="515" y2="16" stroke="#5cb23a" stroke-width="2"/>
    <g fill="#fff" stroke="#5cb23a" stroke-width="2">
      <circle cx="128" cy="22" r="17"/><circle cx="185" cy="22" r="17"/><circle cx="243" cy="22" r="17"/>
      <circle cx="300" cy="22" r="17"/><circle cx="358" cy="22" r="17"/><circle cx="415" cy="22" r="17"/>
    </g>
    <g fill="#5cb23a">
      <rect x="118" y="17" width="12" height="9"/><rect x="131" y="20" width="6" height="6"/><circle cx="122" cy="28" r="2"/><circle cx="134" cy="28" r="2"/>
      <rect x="178" y="13" width="14" height="18" fill="none" stroke="#5cb23a" stroke-width="1.6"/><rect x="181" y="17" width="8" height="1.5"/><rect x="181" y="21" width="8" height="1.5"/><rect x="181" y="25" width="8" height="1.5"/>
    </g>
    <g stroke="#5cb23a" stroke-width="2.4" stroke-linecap="round" fill="none">
      <line x1="236" y1="15" x2="250" y2="29"/><line x1="250" y1="15" x2="236" y2="29"/>
      <path d="M293 22 a7 7 0 1 1 3 6"/><path d="M351 24 a7 7 0 0 1 12 -6 M365 20 a7 7 0 0 1 -12 6"/>
      <circle cx="415" cy="22" r="5"/><circle cx="415" cy="22" r="9" stroke-dasharray="3 2.5"/>
    </g>
  </svg>

  <div class="services">
    <div class="service">
      <svg class="s-icon" width="32" height="32" viewBox="0 0 32 32" aria-hidden="true"><circle cx="16" cy="16" r="15" fill="#fff" stroke="#5cb23a" stroke-width="1.6"/><rect x="7" y="12" width="11" height="8" fill="#5cb23a"/><rect x="19" y="15" width="6" height="5" fill="#5cb23a"/><circle cx="11" cy="22" r="2" fill="#5cb23a"/><circle cx="22" cy="22" r="2" fill="#5cb23a"/></svg>
      <h3>Secure E-Waste Collection Service</h3>
      <ul><li>Flexible and secure end of life and redundant IT asset collection for corporate, small and medium size businesses, government departments, schools and higher learning institutions</li><li>Complete asset tracking through proprietary asset tracking system</li></ul>
    </div>
    <div class="service">
      <svg class="s-icon" width="32" height="32" viewBox="0 0 32 32" aria-hidden="true"><circle cx="16" cy="16" r="15" fill="#fff" stroke="#5cb23a" stroke-width="1.6"/><rect x="10" y="8" width="12" height="16" fill="none" stroke="#5cb23a" stroke-width="1.6"/><rect x="12.5" y="12" width="7" height="1.4" fill="#5cb23a"/><rect x="12.5" y="15.5" width="7" height="1.4" fill="#5cb23a"/><rect x="12.5" y="19" width="7" height="1.4" fill="#5cb23a"/></svg>
      <h3>Certified Data Sanitisation Service</h3>
      <ul><li>Complete data wipe through DOD 5220.22-M certified software</li><li>Physical destruction of HDD and storage media through degaussing and shredding</li><li>Complete asset report (make, model, serial no)</li><li>Certificate of Data Destruction</li></ul>
    </div>
    <div class="service">
      <svg class="s-icon" width="32" height="32" viewBox="0 0 32 32" aria-hidden="true"><circle cx="16" cy="16" r="15" fill="#fff" stroke="#5cb23a" stroke-width="1.6"/><g stroke="#5cb23a" stroke-width="2.6" stroke-linecap="round"><line x1="10" y1="10" x2="22" y2="22"/><line x1="22" y1="10" x2="10" y2="22"/></g></svg>
      <h3>Data Centre Relocation and Decommissioning</h3>
      <ul><li>IT asset deployment, relocation and decommissioning</li><li>Data Centre decommissioning/racking/de-racking and relocation</li><li>Complete cost effective or ad-hoc approach</li></ul>
    </div>
    <div class="service">
      <svg class="s-icon" width="32" height="32" viewBox="0 0 32 32" aria-hidden="true"><circle cx="16" cy="16" r="15" fill="#fff" stroke="#5cb23a" stroke-width="1.6"/><path d="M9 16 a7 7 0 0 1 12 -5 M23 16 a7 7 0 0 1 -12 5" fill="none" stroke="#5cb23a" stroke-width="2"/><circle cx="16" cy="16" r="2.5" fill="#5cb23a"/></svg>
      <h3>IT Asset Remarketing</h3>
      <ul><li>Remarketing of surplus IT equipment</li><li>Competitive pricing for client's surplus assets through our global partners</li><li>Value guaranteed prior to asset collection</li></ul>
    </div>
    <div class="service">
      <svg class="s-icon" width="32" height="32" viewBox="0 0 32 32" aria-hidden="true"><circle cx="16" cy="16" r="15" fill="#fff" stroke="#5cb23a" stroke-width="1.6"/><circle cx="16" cy="16" r="8" fill="none" stroke="#5cb23a" stroke-width="2.4" stroke-dasharray="13 3.8"/></svg>
      <h3>Ewaste Recycling</h3>
      <ul><li>Zero cost to clients for e-waste recycling</li><li>Asset report and certificate of recycling provided upon request</li><li>Focus on reuse prior to recycle and ensure 100% diversion from landfill</li><li>Export to only OECD and BASEL permit approved facility for material recovery</li></ul>
    </div>
    <div class="service">
      <svg class="s-icon" width="32" height="32" viewBox="0 0 32 32" aria-hidden="true"><circle cx="16" cy="16" r="15" fill="#fff" stroke="#5cb23a" stroke-width="1.6"/><circle cx="16" cy="16" r="8" fill="none" stroke="#5cb23a" stroke-width="2.4" stroke-dasharray="3 2.2"/><path d="M14 13 l5 3 l-5 3 z" fill="#5cb23a"/></svg>
      <h3>Logistics Solutions</h3>
      <ul><li>Reverse logistics operations</li><li>Lift Gate service</li><li>Flexible and 24 hour pick up confirmation</li></ul>
    </div>
  </div>

  <div class="industries">
    <h3>Industries Served</h3>
    <p>No matter how big or small your organisation is or how complex or simple your IT systems are, we listen to the needs of your organisation to deliver customized, cost-effective and scalable solution.We ensure data destruction and responsible recycling of your electronic assets are our utmost priority. Our dedicated team is ready to serve you.</p>
    <p class="lead">Industries we serve:</p>
    <ul><li>Corporate</li><li>ITAD Companies</li><li>Financial Institutions</li><li>Educational &amp; Learning Institutions</li><li>Councils</li><li>Recycling companies</li><li>Government sector</li></ul>
  </div>
  <svg class="factory" width="30" height="30" viewBox="0 0 30 30" aria-hidden="true"><circle cx="15" cy="15" r="14" fill="#fff" stroke="#5cb23a" stroke-width="1.6"/><path d="M8 21 V13 l4 3 v-3 l4 3 v-3 l4 3 V9 h2 v12 z" fill="#5cb23a"/></svg>

  <div class="contact-row">
    <span><svg width="10" height="10" viewBox="0 0 10 10" aria-hidden="true"><circle cx="5" cy="5" r="4.5" fill="none" stroke="#5cb23a"/><path d="M3.3 2.8 l1 1 l-.5 .7 l1.5 1.5 l.7 -.5 l1 1 l-.8 .8 c-1.5 0 -3.7 -2.2 -3.7 -3.7 z" fill="#5cb23a"/></svg>1300 46 2587</span>
    <span>48-50 Tannery Road, Ridgefield 2163 NSW</span>
    <span><svg width="10" height="10" viewBox="0 0 10 10" aria-hidden="true"><circle cx="5" cy="5" r="4.5" fill="none" stroke="#5cb23a"/><circle cx="5" cy="5" r="2" fill="#5cb23a"/></svg>www.kelvora-scrap.com.au</span>
  </div>

  <div class="footer-bars">
    <i style="width:10%;background:var(--green)"></i><i style="width:12%;background:var(--teal)"></i><i style="width:20%;background:var(--forest)"></i><i style="width:58%;background:var(--slate)"></i>
  </div>
</section>

</body>
</html>
```